Communication and Marketing agency needs a new presentation card

We are a group of communication and marketing agencies specialized in companies that are in the logistics and industrial sector. The head agency is TELVANO Grupo and the group consists of 4 agencies: TELVANO Media, TELVANO Digital, TELVANO Research and EnlazaPorImagen. We hace 4 offices in Spain (Madrid, Barcelona, Valencia and Murcia). We are looking for a clean and attractive design that transmits our experience, brand presence in the market and knowledge to those who receive the card.It has to maintain the colors of the logo that is attached.
Target Market(s)
logistics and industrial sector
Marketing department
Clean and attractive design

```html
<!DOCTYPE html>
<html lang="es">
<head>
<meta charset="utf-8">
<title>TELVANO Grupo – Tarjeta de presentación</title>
<link rel="stylesheet" href="https://fonts.googleapis.com/css2?family=Open+Sans:wght@400;600&family=Roboto:wght@500;700&display=swap">
<style>
  :root{
    --brand-red:#b41c2a;
    --ink:#2e2e2e;
    --ink-soft:#555;
    --card-white:#ffffff;
    --backdrop:#ececec;
  }
  *{margin:0;padding:0;box-sizing:border-box}
  html,body{width:1200px;height:900px;overflow:hidden}
  body{background:var(--backdrop);position:relative;font-family:"Open Sans",Arial,sans-serif;color:var(--ink)}

  .card{position:absolute;width:556px;height:343px;box-shadow:0 3px 8px rgba(0,0,0,.25)}
  .card--front{left:330px;top:90px;background:var(--card-white)}
  .card--back{left:330px;top:470px;background:var(--brand-red)}

  .front__band{position:absolute;left:0;right:0;bottom:0;height:12px;background:var(--brand-red)}

  .brand-name{font-family:"Open Sans",Arial,sans-serif;font-weight:600;line-height:1;letter-spacing:1px}
  .brand-name small{display:block;font-size:.5em;text-align:right;letter-spacing:0;margin-top:6px}

  .front__logo{position:absolute;left:32px;top:48px;font-size:40px;color:var(--brand-red);width:240px}

  .person{position:absolute;right:34px;top:55px;text-align:right}
  .person__name{font-family:"Roboto",Arial,sans-serif;font-weight:700;font-size:19px;color:var(--brand-red);letter-spacing:.3px}
  .person__role{font-size:15px;color:var(--ink);margin-top:1px}

  .contact{position:absolute;left:30px;top:235px;list-style:none}
  .contact li{display:flex;align-items:center;gap:6px;font-size:15.5px;line-height:20.3px;color:var(--ink)}
  .contact svg{width:11px;height:11px;fill:var(--brand-red);flex:none}

  .agencies{position:absolute;right:34px;top:232px;display:grid;grid-template-columns:auto auto;column-gap:12px;row-gap:10px;justify-items:end}
  .agency{font-size:16px;text-align:right}
  .agency small{font-size:11px;margin-top:2px}
  .agency--grey{color:var(--ink-soft)}
  .agency--red{color:var(--brand-red)}

  .back__logo{position:absolute;left:142px;top:128px;width:272px;font-size:46px;color:var(--card-white)}
  .back__cities{position:absolute;left:0;right:0;top:290px;text-align:center;font-size:15px;color:var(--card-white);letter-spacing:.3px}
</style>
</head>
<body>

<section class="card card--front" aria-label="Anverso de la tarjeta">
  <div class="brand-name front__logo">TELVANO<small>Grupo</small></div>

  <div class="person">
    <p class="person__name">MARTA QUIROGA</p>
    <p class="person__role">Managing Director</p>
  </div>

  <ul class="contact">
    <li><svg viewBox="0 0 12 12"><path d="M1 4c0-1.5 2-3 5-3s5 1.5 5 3v1H8.5V3.5h-5V5H1zM2 6h8l1 5H1z"/></svg>091-482 730 516</li>
    <li><svg viewBox="0 0 12 12"><path d="M3 0h6a1 1 0 0 1 1 1v10a1 1 0 0 1-1 1H3a1 1 0 0 1-1-1V1a1 1 0 0 1 1-1zm0 1.5v8h6v-8zM6 10.2a.6.6 0 1 0 0 1.2.6.6 0 0 0 0-1.2z"/></svg>091-482 730 517</li>
    <li><svg viewBox="0 0 12 12"><path d="M0 2h12v1.2L6 7 0 3.2zM0 4.6l6 3.8 6-3.8V10H0z"/></svg>hola@telvanogrupo.es</li>
    <li><svg viewBox="0 0 12 12"><circle cx="6" cy="6" r="6"/></svg>www.telvanogrupo.es</li>
  </ul>

  <div class="agencies">
    <div class="brand-name agency agency--grey">TELVANO<small>Research</small></div>
    <div class="brand-name agency agency--grey">TELVANO<small>Digital</small></div>
    <div class="brand-name agency agency--red">TELVANO<small>Media</small></div>
    <div class="brand-name agency agency--red">EnlazaPorImagen</div>
  </div>

  <div class="front__band"></div>
</section>

<section class="card card--back" aria-label="Reverso de la tarjeta">
  <div class="brand-name back__logo">TELVANO<small>Grupo</small></div>
  <p class="back__cities">MADRID, BARCELONA, VALENCIA, MURCIA</p>
</section>

</body>
</html>
```